Corvella Paintless Dent Removal

Our company works on vehicles removing dents using a highly skilled trade which the metal is massaged out with special tools without disturbing the original paint, hence paintless dent removal. Besides keeping the paint and metal original its also very environmentally friendly since no paint or toxic fillers are used. Also we we are one of the most experienced companies in the business with 25 years

Target Market(s)

Retail Automobile consumers, Auto Dealerships and Auto Body Shops

Industry/Entity Type

Auto Repair

Contact Information for Business Card

Dennis Holbrook
PO Box 538 Ashmere, NY 11952
631-472-8816
corvellapdr@mailnest.example
website corvellapdr.example
youtube corvella paintless dent removal
25 years of experience removing Dents, Dings and Hail Damage

Font styles to use
Serif
Sans Serif

Colors

Designer to choose colors to be used in the design.

Requirements
Must have
• I do like things that are simple but classy and somewhat bold, also I like my logo so that should be somewhat important

```html
<!DOCTYPE html>
<html lang="en">
<head>
<meta charset="utf-8">
<title>Corvella Paintless Dent Removal – Business Card</title>
<link href="https://fonts.googleapis.com/css2?family=Open+Sans:ital,wght@0,400;0,700;0,800;1,400&display=swap" rel="stylesheet">
<style>
  :root {
    --backdrop: #c8b199;
    --paper: #ffffff;
    --navy: #0f2a4f;
    --green: #76c128;
    --ink: #3a3a3a;
    --muted: #6b6b6b;
  }
  * { margin: 0; padding: 0; box-sizing: border-box; }
  html, body {
    width: 1200px; height: 1200px; overflow: hidden;
    background: var(--backdrop);
    font-family: "Open Sans", Arial, sans-serif;
  }
  .canvas {
    width: 1200px; height: 1200px;
    display: flex; flex-direction: column; align-items: center; justify-content: center;
    gap: 80px;
  }
  .card {
    position: relative;
    width: 700px; height: 400px;
    background: var(--paper);
    overflow: hidden;
    box-shadow: 0 14px 30px rgba(60, 40, 20, 0.25);
  }
  .card__art { position: absolute; inset: 0; }

  /* Front */
  .contact-list {
    position: absolute; left: 44px; top: 218px;
    list-style: none;
    font-size: 15px; line-height: 25px; color: var(--ink);
  }
  .contact-list li { display: flex; align-items: center; gap: 10px; }
  .contact-icon { width: 14px; height: 14px; flex: none; }
  .identity {
    position: absolute; left: 392px; top: 34px;
    color: var(--navy);
  }
  .identity__brand { font-size: 30px; font-weight: 800; line-height: 1; letter-spacing: 0.5px; }
  .identity__sub { font-size: 15px; font-weight: 700; line-height: 1.2; margin-bottom: 14px; }
  .identity__name { font-size: 20px; font-weight: 800; line-height: 1.1; letter-spacing: 0.5px; }
  .identity__role { font-size: 15px; font-weight: 700; color: var(--ink); }

  /* Back */
  .wordmark {
    position: absolute; left: 0; right: 0; top: 150px;
    display: flex; flex-direction: column; align-items: center;
    color: var(--navy);
  }
  .wordmark__name { font-size: 40px; font-weight: 800; line-height: 1; letter-spacing: 1px; display: flex; align-items: center; gap: 12px; }
  .wordmark__dot { width: 16px; height: 16px; border-radius: 50%; background: var(--green); }
  .wordmark__sub { font-size: 40px; font-weight: 800; line-height: 1.1; font-size: 20px; }
  .tagline {
    margin-top: 14px;
    font-size: 12px; font-style: italic; color: var(--muted);
  }
</style>
</head>
<body>
<main class="canvas">

  <section class="card card--front" aria-label="Business card front">
    <svg class="card__art" viewBox="0 0 700 400" aria-hidden="true">
      <g fill="var(--green)">
        <path d="M0 0 H50 V95 A50 50 0 0 1 0 120 Z"/>
        <path d="M66 0 H126 V110 A60 60 0 0 1 66 120 Z"/>
        <path d="M142 0 H230 V70 A100 100 0 0 1 142 120 Z"/>
      </g>
      <g fill="var(--navy)">
        <path d="M700 400 H640 V330 A60 60 0 0 1 700 250 Z"/>
        <path d="M622 400 H562 V310 A70 70 0 0 1 622 250 Z"/>
        <path d="M544 400 H440 V330 A110 110 0 0 1 544 250 Z"/>
      </g>
    </svg>

    <ul class="contact-list">
      <li>
        <svg class="contact-icon" viewBox="0 0 14 14"><circle cx="7" cy="7" r="7" fill="var(--green)"/><path d="M4.5 3.5l1.5 0 .6 1.8-.9.7a5 5 0 0 0 2.3 2.3l.7-.9 1.8.6v1.5c-3.5.5-6.5-2.5-6-6z" fill="var(--navy)"/></svg>
        631-472-8816
      </li>
      <li>
        <svg class="contact-icon" viewBox="0 0 14 14"><circle cx="7" cy="7" r="7" fill="var(--green)"/><rect x="3.5" y="4.5" width="7" height="5" fill="none" stroke="var(--navy)" stroke-width="1"/><path d="M3.5 4.5l3.5 3 3.5-3" fill="none" stroke="var(--navy)" stroke-width="1"/></svg>
        corvellapdr@mailnest.example
      </li>
      <li>
        <svg class="contact-icon" viewBox="0 0 14 14"><circle cx="7" cy="7" r="7" fill="var(--green)"/><circle cx="7" cy="7" r="3.6" fill="none" stroke="var(--navy)" stroke-width="1"/><path d="M3.4 7h7.2M7 3.4c-2 2.4-2 4.8 0 7.2M7 3.4c2 2.4 2 4.8 0 7.2" fill="none" stroke="var(--navy)" stroke-width=".8"/></svg>
        corvellapdr.example
      </li>
      <li>
        <svg class="contact-icon" viewBox="0 0 14 14"><circle cx="7" cy="7" r="7" fill="var(--green)"/><path d="M7 11s-3-3.2-3-5.2a3 3 0 0 1 6 0C10 7.8 7 11 7 11z" fill="var(--navy)"/><circle cx="7" cy="5.8" r="1" fill="var(--green)"/></svg>
        PO Box 538 Ashmere, NY 11952
      </li>
      <li>
        <svg class="contact-icon" viewBox="0 0 14 14"><circle cx="7" cy="7" r="7" fill="var(--green)"/><path d="M5.5 4.5v5l4-2.5z" fill="var(--navy)"/></svg>
        corvella paintless dent removal
      </li>
    </ul>

    <div class="identity">
      <p class="identity__brand">CORVELLA</p>
      <p class="identity__sub">Paintless Dent Removal</p>
      <p class="identity__name">DENNIS HOLBROOK</p>
      <p class="identity__role">Designation</p>
    </div>
  </section>

  <section class="card card--back" aria-label="Business card back">
    <svg class="card__art" viewBox="0 0 700 400" aria-hidden="true">
      <path d="M0 40 A40 40 0 0 1 24 4 V400 H0 Z" fill="var(--green)"/>
      <path d="M672 0 H700 V400 A40 40 0 0 1 672 372 Z" fill="var(--navy)"/>
    </svg>
    <div class="wordmark">
      <p class="wordmark__name"><span class="wordmark__dot"></span>CORVELLA</p>
      <p class="wordmark__sub">Paintless Dent Removal</p>
      <p class="tagline">25 years of experience removing Dents, Dings and Hail Damage</p>
    </div>
  </section>

</main>
</body>
</html>
```